依頼詳細
引越を考えているお客様にチラシを渡して頂くため、不動産店舗を回って交渉をしています。
その際に営業の皆様に渡す名刺です。
「引越業者選び面倒臭い!とお思いの皆様へ。」
「数多くある引越業者から安くしっかりした業者を選定してくれる」「面倒なことを全て引き受けてくれる」ことが売りの会社です。

チラシはお客様向けなのでポップな雰囲気で分かり易く作って頂いていますが、名刺のデザインとしては
信頼感や堅実さを押し出すのが良いのかなと思っています。

添付のファイルは会社のロゴです。

それでは宜しくお願いいたします。
記載項目
株式会社brightway/役職名/佐藤 健一/KENICHI SATO/本社所在地 〒105-0021 東京都港区東新橋4-2-8/代表 03-5417-3861/お見積専用ダイヤル0120-583-216/HP www.bwaymv.co.jp/Mail info.bwaymv.co.jp/
希望イメージ
シンプル 複雑
単色 カラフル
暗い 明るい
日常 高級
遊び心 厳粛
未来的 伝統的
女性的 男性的
希望する色
納品ファイル
• 高解像度JPG (.jpg)
• イラストレーター形式 (.ai)
補足説明
添付しましたイラストレーターファイル(会社ロゴ)につきまして、バージョンが新しいために開けない、古く出来ないかとのご相談がありました。
取り急ぎ、解像度が粗いですがjpgファイルを添付しますので、仮でこれをお使い下さい。

どれを使ってあっても、全体のデザインが気に入れば採用します。
■ 選んだ理由

お伝えしたかった意図をよく汲んで頂いたこと、見た目の爽やかさと分かりやすさが決め手となりました。
こちらからの要望も気持ち良く受けて頂き、感謝しています。

■ 提案者全員のお礼・コメント

とても素晴らしいご提案を沢山頂きました。
惜しくも選外とさせて頂いた方も、また別の機会にお付き合い頂ければ幸いです。

```html
<!DOCTYPE html>
<html lang="ja">
<head>
<meta charset="UTF-8">
<title>株式会社brightway 名刺</title>
<link rel="stylesheet" href="https://fonts.googleapis.com/css2?family=Noto+Sans+JP:wght@400;500;700&family=Cormorant+Garamond:ital,wght@1,500&display=swap">
<style>
  :root {
    --blue: #5ba9dc;
    --green: #8cc63f;
    --ink: #333333;
    --ink-soft: #666666;
    --paper: #ffffff;
    --paper-back: #eeeeef;
    --faint: #eeeeee;
    --stage: #ffffff;
  }
  * { box-sizing: border-box; margin: 0; padding: 0; }
  html, body {
    width: 841px; height: 1200px; overflow: hidden;
    background: var(--stage);
    font-family: "Noto Sans JP", sans-serif;
    color: var(--ink);
  }
  .card {
    position: absolute; left: 70px; width: 700px; height: 448px;
    box-shadow: 0 2px 8px rgba(0,0,0,0.25);
    overflow: hidden;
  }
  .card--front { top: 84px; background: var(--paper); }
  .card--back { top: 658px; background: var(--paper-back); }

  .edge-bar { position: absolute; left: 0; width: 16px; }
  .edge-bar--blue { top: 0; height: 280px; background: var(--blue); }
  .edge-bar--green { top: 280px; height: 168px; background: var(--green); }
  .bottom-line { position: absolute; left: 0; bottom: 0; width: 100%; height: 5px; background: var(--green); }

  .faint-mark {
    position: absolute; left: 470px; top: 180px; width: 240px; height: 240px;
    border-radius: 50%; background: var(--faint);
  }

  .brand { position: absolute; display: flex; align-items: center; gap: 14px; }
  .brand__square { width: 46px; height: 46px; background: var(--blue); }
  .brand__name { font-family: "Noto Sans JP", sans-serif; font-weight: 700; color: var(--green); letter-spacing: 0.5px; }
  .card--front .brand { left: 400px; top: 64px; }
  .card--front .brand__name { font-size: 40px; }

  .person { position: absolute; left: 70px; top: 92px; }
  .person__title { font-size: 13px; color: var(--ink); }
  .person__name { font-size: 34px; font-weight: 500; letter-spacing: 10px; margin-top: 4px; }
  .person__roman { font-family: "Cormorant Garamond", serif; font-style: italic; font-size: 21px; color: var(--ink-soft); margin-top: 8px; }

  .company { position: absolute; left: 70px; top: 250px; font-size: 24px; font-weight: 700; }

  .contacts { position: absolute; left: 70px; top: 298px; list-style: none; }
  .contacts li { display: flex; align-items: center; gap: 10px; font-size: 14px; height: 26px; }
  .contacts svg { width: 16px; height: 16px; flex: none; }
  .freedial-badge { width: 28px; height: 14px; border-radius: 2px; background: var(--green); flex: none; margin-left: -6px; }

  .card--back .brand { left: 0; right: 0; top: 150px; flex-direction: column; gap: 18px; }
  .card--back .brand__square { width: 80px; height: 80px; }
  .card--back .brand__name { font-size: 50px; }
  .back-bands { position: absolute; left: 0; bottom: 0; width: 700px; height: 40px; }
</style>
</head>
<body>
  <section class="card card--front" aria-label="名刺 表面">
    <div class="edge-bar edge-bar--blue"></div>
    <div class="edge-bar edge-bar--green"></div>
    <div class="faint-mark"></div>

    <div class="brand">
      <span class="brand__square"></span>
      <span class="brand__name">brightway</span>
    </div>

    <div class="person">
      <p class="person__title">代表取締役</p>
      <p class="person__name">佐藤 健一</p>
      <p class="person__roman">Kenichi Sato</p>
    </div>

    <p class="company">株式会社brightway</p>

    <ul class="contacts">
      <li>
        <svg viewBox="0 0 16 16"><path d="M8 1a5 5 0 0 0-5 5c0 4 5 9 5 9s5-5 5-9a5 5 0 0 0-5-5zm0 7a2 2 0 1 1 0-4 2 2 0 0 1 0 4z" fill="var(--green)"/></svg>
        〒105-0021 東京都港区東新橋4-2-8
      </li>
      <li>
        <svg viewBox="0 0 16 16"><path d="M4 1.5l2.5 3-1.5 1.5c.8 2 2.5 3.7 4.5 4.5l1.5-1.5 3 2.5-1.5 2.5C7 14 2 9 1.5 3z" fill="var(--green)"/></svg>
        03-5417-3861
      </li>
      <li>
        <svg viewBox="0 0 16 16"><rect x="1.5" y="3.5" width="13" height="9" fill="none" stroke="var(--green)" stroke-width="1.5"/><path d="M1.5 3.5l6.5 5 6.5-5" fill="none" stroke="var(--green)" stroke-width="1.5"/></svg>
        info.bwaymv.co.jp
      </li>
      <li>
        <svg viewBox="0 0 16 16"><circle cx="8" cy="8" r="6.5" fill="none" stroke="var(--green)" stroke-width="1.5"/><ellipse cx="8" cy="8" rx="2.8" ry="6.5" fill="none" stroke="var(--green)" stroke-width="1.2"/><path d="M1.5 8h13" stroke="var(--green)" stroke-width="1.2"/></svg>
        https://www.bwaymv.co.jp
      </li>
      <li>
        <span class="freedial-badge"></span>
        0120-583-216
      </li>
    </ul>

    <div class="bottom-line"></div>
  </section>

  <section class="card card--back" aria-label="名刺 裏面">
    <div class="brand">
      <span class="brand__square"></span>
      <span class="brand__name">brightway</span>
    </div>
    <svg class="back-bands" viewBox="0 0 700 40" preserveAspectRatio="none">
      <polygon points="0,22 470,22 452,40 0,40" fill="var(--green)"/>
      <polygon points="478,22 700,22 700,40 460,40" fill="var(--blue)"/>
    </svg>
  </section>
</body>
</html>
```